Business Card Design Project

I am a psychotherapist, counselor and expressive arts therapist (means I use every art form imaginable in the service of healing). I'm just starting out in private practice in San Francisco, CA. I work with individual adults, children and families. I'd like the card to mirror the simplicity and color palate of my website. I also would love if there is a symbol, image of fire, flame or spark (that is warming, not frightening).

Check out my website: www.lorabecketmft.com

I want the cards to be printed in letter press so please keep that in mind!

Target Market(s)

Upper Middle Class Adults who are progressively minded, artistic or artists, open to psychotherapy, interested in health & healing.

Industry/Entity Type

Business

Requirements
Must have
• Text to be included:

Lora Becket
Counseling, Psychotherapy & Expressive Arts

2914 Alderwood Avenue, Suite D
San Francisco, CA 94127
p. 415.206.3791
lorajanebecket@meadowpost.net

www.lorabecketmft.com

MFT License Number 48671

It's OK to abbreviate Number to # or Street to St., etc.

Must be compatible with letter press printing.
Nice to have
• I don't have a logo. I don't expect designers to necessarily create one for me, but if someone comes up with a simple image (see above about flame), that would be great. I don't have much of a budget now, but expect that to change in the next year or so and then could buy a logo for my website, future letterhead, etc.

```html
<!DOCTYPE html>
<html lang="en">
<head>
<meta charset="utf-8">
<title>Lora Becket — Business Card</title>
<link rel="stylesheet" href="https://fonts.googleapis.com/css2?family=Cutive+Mono&family=Lato:ital,wght@0,400;1,400&display=swap">
<style>
  :root {
    --backdrop: #2e2e2f;
    --card-peach: #fcd5b1;
    --name-red: #d03a50;
    --ink: #2b2724;
  }
  * { margin: 0; padding: 0; box-sizing: border-box; }
  html, body {
    width: 1200px;
    height: 900px;
    overflow: hidden;
    background: var(--backdrop);
  }
  .canvas {
    width: 1200px;
    height: 900px;
    display: flex;
    align-items: center;
    justify-content: center;
  }
  .business-card {
    position: relative;
    width: 1050px;
    height: 600px;
    background: var(--card-peach);
    color: var(--ink);
    font-family: "Lato", Arial, sans-serif;
  }
  .practitioner-name {
    position: absolute;
    left: 170px;
    top: 62px;
    font-family: "Cutive Mono", "Courier New", monospace;
    font-weight: 400;
    font-size: 100px;
    letter-spacing: 2px;
    color: var(--name-red);
    white-space: nowrap;
    line-height: 1;
  }
  .practice-tagline {
    position: absolute;
    right: 180px;
    top: 180px;
    font-style: italic;
    font-size: 26px;
    white-space: nowrap;
  }
  .office-details {
    position: absolute;
    left: 250px;
    top: 258px;
    font-style: normal;
    font-size: 29px;
    line-height: 1.22;
    white-space: nowrap;
  }
  .office-details span { display: block; }
  .office-details .indented { padding-left: 14px; }
  .license-number {
    position: absolute;
    left: 222px;
    top: 490px;
    font-size: 29px;
    white-space: nowrap;
  }
</style>
</head>
<body>
  <main class="canvas">
    <section class="business-card" aria-label="Business card front">
      <h1 class="practitioner-name">LORA BECKET</h1>
      <p class="practice-tagline">Counseling, Psychotherapy &amp; Expressive Arts</p>
      <address class="office-details">
        <span class="street-line">2914 Alderwood Avenue, Suite D</span>
        <span class="city-line indented">San Francisco, CA 94127</span>
        <span class="phone-line indented">phone: 415.206.3791</span>
        <span class="email-line indented">lorajanebecket@meadowpost.net</span>
        <span class="web-line indented">www.lorabecketmft.com</span>
      </address>
      <p class="license-number">MFT License Number 48671</p>
    </section>
  </main>
</body>
</html>
```